Wordpress Design Project - QuorvanLabs

I would like our existing old website at www.quorvanlabs.example to be redesigned to a more modern attractive site using Wordpress, a total of 5 web pages. And also installed onto our new web hosting site. Please visit the existing website using Microsoft Internet explorer to see the content.
The new site must be compatible with all popular web browsers and mobile devices (if possible).
There should be a contact button available on each page with an associated form in case an interested person wants to contact us. This form must be spam proof not allowing automated crawlers from activating it.
Updates

There are only 5 pages web pages to this QuorvanLabs project.

Industry/Entity Type

Internet

```html
<!DOCTYPE html>
<html lang="en">
<head>
<meta charset="utf-8">
<title>QuorvanLabs</title>
<link href="https://fonts.googleapis.com/css2?family=Dosis:wght@400;500;600;700&family=Roboto:wght@300;400;500&family=Roboto+Condensed:wght@300;400&display=swap" rel="stylesheet">
<style>
:root{
  --dark:#333333;
  --blue:#3b7096;
  --blue-deep:#2f6287;
  --brand:#1f5fa6;
  --accent:#f5b52a;
  --ink:#2f5f82;
  --panel:#f7f7f7;
  --page:#e6e6e6;
  --muted:#7d7d7d;
  --soft:#c4c4c4;
  --green:#6f9a2c;
}
*{margin:0;padding:0;box-sizing:border-box}
html,body{width:1179px;height:1200px;overflow:hidden}
body{position:relative;background:var(--page);font-family:'Roboto',sans-serif}
.topbar{position:absolute;left:0;top:0;width:1179px;height:53px;background:var(--dark)}
.topbar-note{position:absolute;right:122px;top:24px;color:#fff;font:300 18px 'Roboto',sans-serif}
.blue-band{position:absolute;left:0;top:53px;width:1179px;height:467px;background:linear-gradient(180deg,var(--blue),var(--blue-deep))}
.dark-band{position:absolute;left:0;top:520px;width:1179px;height:77px;background:var(--dark)}
.logo{position:absolute;left:124px;top:0;width:295px;height:107px;background:#fff}
.logo-mark{position:absolute;left:18px;top:28px;width:50px;height:50px;border-radius:50%;background:var(--brand)}
.logo-name{position:absolute;left:84px;top:32px;color:var(--brand);font:700 29px 'Roboto',sans-serif}
.logo-tag{position:absolute;left:86px;top:67px;color:var(--brand);font:500 8px 'Roboto',sans-serif}
.nav{position:absolute;right:122px;top:70px;display:flex;gap:10px;color:var(--accent);font:700 24px 'Dosis',sans-serif}
.hero{position:absolute;left:124px;top:120px;width:933px;height:353px;background:linear-gradient(90deg,#d9ddd8 0%,#b9bcbc 45%,#8b8d8f 70%,#d6d3cd 100%)}
.callout{position:absolute;left:91px;top:505px;width:997px;height:80px;background:linear-gradient(180deg,#3a3a3a,#262626);box-shadow:0 3px 6px rgba(0,0,0,.4);color:#fff;text-align:center;font:400 33px/80px 'Dosis',sans-serif;letter-spacing:-.5px}
.callout b{font-weight:700}
.content{position:absolute;left:124px;top:585px;width:933px;height:570px;background:var(--panel)}
.feature{position:absolute;width:300px}
.feature-icon{position:absolute;left:-82px;top:4px;width:60px;height:60px}
.feature h2{color:var(--ink);font:700 21px 'Dosis',sans-serif;letter-spacing:-.3px}
.feature p{margin-top:2px;color:var(--muted);font:300 12.5px/17px 'Roboto Condensed',sans-serif;letter-spacing:-.3px}
.newsletter{position:absolute;left:24px;top:293px;width:885px;height:66px;background:#efefef;border-top:1px solid #e0e0e0}
.newsletter-text{position:absolute;left:35px;top:28px;color:#888;font:400 13.5px 'Roboto',sans-serif}
.newsletter-text b{font-weight:500;color:#777}
.email-field{position:absolute;left:505px;top:13px;width:308px;height:45px;background:#fff;border:1px solid #ccc;border-radius:5px 0 0 5px;padding:14px 21px;color:#444;font:400 13px 'Roboto',sans-serif}
.go{position:absolute;left:812px;top:13px;width:53px;height:45px;background:linear-gradient(180deg,#86b23c,var(--green));border-radius:0 5px 5px 0;color:#fff;text-align:center;font:700 28px/45px 'Dosis',sans-serif}
.rule{position:absolute;left:24px;top:392px;width:885px;height:1px;background:#e2e2e2}
.slogan{position:absolute;left:0;top:410px;width:933px;text-align:center;color:var(--soft);font:600 44px 'Dosis',sans-serif}
.contact-line{position:absolute;left:0;top:473px;width:933px;text-align:center;color:var(--ink);font:400 23px 'Dosis',sans-serif}
.contact-line b{font-weight:600}
.foot-strip{position:absolute;left:0;top:522px;width:933px;height:48px;background:#eeeeee}
.to-top{position:absolute;right:0;top:0;width:44px;height:48px;background:#fff;border:1px solid #e0e0e0}
.copyright{position:absolute;left:153px;top:1166px;color:#888;font:300 12px 'Roboto Condensed',sans-serif}
.copyright span{color:var(--ink)}
.social{position:absolute;left:981px;top:1168px;display:flex;gap:5px}
.social i{display:block;width:15px;height:15px;border-radius:2px}
</style>
</head>
<body>
<div class="topbar"><p class="topbar-note">We offer 24 hour worldwide Technical Support!</p></div>
<div class="blue-band"></div>
<div class="dark-band"></div>

<header class="logo">
  <span class="logo-mark"></span>
  <span class="logo-name">QuorvanLabs</span>
  <span class="logo-tag">A Leading Edge Technology Company</span>
</header>
<nav class="nav"><span>Home</span><span>|</span><span>VoIP</span><span>|</span><span>Internet</span><span>|</span><span>Support</span><span>|</span><span>Contact</span></nav>

<div class="hero" role="img" aria-label="Photo of an office desk phone beside a pen cup and plant"></div>

<div class="callout">Call our <b>toll free</b> number today <b>1888 555 0142</b>.</div>

<main class="content">
  <section class="feature" style="left:153px;top:85px">
    <svg class="feature-icon" viewBox="0 0 60 60"><path fill="var(--ink)" d="M14 6c3-2 6-1 7 2l4 9c1 3 0 5-2 6l-3 2c2 6 8 12 14 14l2-3c1-2 3-3 6-2l9 4c3 1 4 4 2 7l-3 5c-2 3-6 4-10 3C25 48 12 35 7 20c-1-4 0-8 3-10z"/></svg>
    <h2>Telephone VoIP Solutions</h2>
    <p>Lorem Ipsum is simply dummy text of the printing and typesetting industry. Lorem Ipsum has been the industry's standard dummy text ever since the 1500s</p>
  </section>
  <section class="feature" style="left:593px;top:85px">
    <svg class="feature-icon" viewBox="0 0 60 60"><circle cx="30" cy="30" r="27" fill="var(--ink)"/><path fill="#fff" d="M14 17c6-2 10 1 11 5s-3 6-2 10 5 5 3 11c-6-3-10-10-12-16zM34 10c5 1 9 4 10 8-3 1-6-1-9-3z"/></svg>
    <h2>Wired / Wireless Internet</h2>
    <p>Lorem Ipsum is simply dummy text of the printing and typesetting industry. Lorem Ipsum has been the industry's standard dummy text ever since the 1500s</p>
  </section>
  <section class="feature" style="left:153px;top:207px">
    <svg class="feature-icon" viewBox="0 0 60 60"><g fill="var(--ink)"><circle cx="22" cy="32" r="13"/><circle cx="44" cy="17" r="8"/><circle cx="44" cy="44" r="8"/></g><g fill="var(--panel)"><circle cx="22" cy="32" r="5"/><circle cx="44" cy="17" r="3"/><circle cx="44" cy="44" r="3"/></g></svg>
    <h2>LAN, WAN &amp; IP Services</h2>
    <p>Lorem Ipsum is simply dummy text of the printing and typesetting industry. Lorem Ipsum has been the industry's standard dummy text ever since the 150s</p>
  </section>
  <section class="feature" style="left:593px;top:207px">
    <svg class="feature-icon" viewBox="0 0 70 60"><g fill="var(--ink)"><ellipse cx="27" cy="25" rx="24" ry="16"/><path d="M12 36l-4 10 14-7z"/><ellipse cx="46" cy="37" rx="20" ry="13" stroke="var(--panel)" stroke-width="3"/><path d="M56 46l6 8-14-6z"/></g></svg>
    <h2>24 Hour Help Desk</h2>
    <p>Lorem Ipsum is simply dummy text of the printing and typesetting industry. Lorem Ipsum has been the industry's standard dummy text ever since the 1500s</p>
  </section>

  <div class="newsletter">
    <p class="newsletter-text"><b>Subscribe to our newsletter</b> to stay up to date with our latest offers</p>
    <div class="email-field">Enter your email here...</div>
    <div class="go">GO</div>
  </div>
  <div class="rule"></div>
  <p class="slogan">‘Quorvan Labs, Your Network Expert!’</p>
  <p class="contact-line"><b>Phone</b> 1888 555 0142 &nbsp;|&nbsp; <b>Local</b> (807) 555.0199 &nbsp;|&nbsp; <b>Email</b> info@quorvanlabs.example</p>
  <div class="foot-strip">
    <div class="to-top"><svg width="44" height="48" viewBox="0 0 44 48"><path d="M22 17l-6 6h4v8h4v-8h4z" fill="var(--ink)"/></svg></div>
  </div>
</main>

<p class="copyright">© Copyright 2013 <span>QuorvanLabs Inc.</span> All rights reserved.</p>
<div class="social"><i style="background:#55acee"></i><i style="background:#3b5998"></i><i style="background:#555"></i></div>
</body>
</html>
```